Kestmar Conflict Varnok Legion Memoir Book Cover Design

We need a book cover design for a Russian kestmar conflict memoir.
Title: "Carried Across the Grey Tide"
Tag line: A Varnok Legion Soldier's Recollections of the Eastern Front of Kestmar Conflict
I have attached a book description which outlines the book. This is to go on the back cover.
I have attached images of book covers of the style we are looking for. Being Russia and War.
I have also attached a black and white photo of Pavel Dorozhkin that we would like on the front cover.
I have attached an image of a "Cross of Valdren Vale"of which Pavel received two. If an image of this could be incorporated on the front or back.
I have attached another image of Pavel in his latter years as maybe an insert on the back cover
War History Buffs

```html
<!DOCTYPE html>
<html lang="en">
<head>
<meta charset="utf-8">
<title>Carried Across the Grey Tide – Book Cover</title>
<link href="https://fonts.googleapis.com/css2?family=Bebas+Neue&family=Jost:wght@400&display=swap" rel="stylesheet">
<style>
  :root {
    --stage: #ececec;
    --paper: #f1f1f1;
    --paper-shade: #dcdcdc;
    --crimson: #b30d12;
    --ink: #231f20;
    --tag-ink: #2b2b2b;
    --photo-grey: #8a8a86;
    --photo-dark: #55564f;
    --photo-red: #9c1b1f;
  }
  html, body {
    margin: 0;
    width: 1200px;
    height: 1200px;
    overflow: hidden;
    background: var(--stage);
  }
  .cover {
    position: absolute;
    left: 230px;
    top: 30px;
    width: 740px;
    height: 1140px;
    overflow: hidden;
    background: radial-gradient(ellipse at 35% 40%, #f7f7f7 0%, var(--paper) 55%, var(--paper-shade) 100%);
    box-shadow: 0 4px 18px rgba(0,0,0,0.18);
  }
  .portrait {
    position: absolute;
    left: 300px;
    top: 150px;
    width: 440px;
    height: 990px;
    background:
      radial-gradient(ellipse 55% 18% at 58% 22%, rgba(160,160,160,0.9) 0%, rgba(200,200,200,0) 100%),
      radial-gradient(ellipse 40% 20% at 62% 42%, rgba(170,150,150,0.85) 0%, rgba(200,200,200,0) 100%),
      radial-gradient(ellipse 30% 32% at 8% 78%, rgba(156,27,31,0.75) 0%, rgba(156,27,31,0) 100%),
      linear-gradient(180deg, rgba(241,241,241,0) 0%, var(--photo-grey) 45%, var(--photo-dark) 75%, rgba(241,241,241,0.2) 100%);
    -webkit-mask-image: radial-gradient(ellipse 75% 70% at 70% 55%, #000 55%, transparent 100%);
            mask-image: radial-gradient(ellipse 75% 70% at 70% 55%, #000 55%, transparent 100%);
  }
  .tagline {
    position: absolute;
    left: 68px;
    top: 72px;
    margin: 0;
    font-family: "Jost", sans-serif;
    font-weight: 400;
    font-size: 31px;
    line-height: 1.38;
    color: var(--tag-ink);
  }
  .title {
    position: absolute;
    left: 74px;
    top: 236px;
    margin: 0;
    font-family: "Bebas Neue", sans-serif;
    font-weight: 400;
    font-size: 150px;
    line-height: 143px;
    letter-spacing: 1px;
  }
  .title span { display: block; }
  .title .red { color: var(--crimson); }
  .title .dark { color: var(--ink); }
  .author {
    position: absolute;
    left: 74px;
    top: 888px;
    margin: 0;
    font-family: "Bebas Neue", sans-serif;
    font-weight: 400;
    font-size: 78px;
    line-height: 70px;
    color: var(--crimson);
  }
  .author span { display: block; }
</style>
</head>
<body>
  <main class="cover">
    <div class="portrait" role="img" aria-label="Tinted black and white portrait photograph of Pavel Dorozhkin in a fur winter hat and military tunic with medals"></div>
    <p class="tagline">A Varnok Legion Soldier's<br>Recollections of the Eastern Front<br>of Kestmar Conflict</p>
    <h1 class="title">
      <span class="red">Carried</span>
      <span class="red">Across</span>
      <span class="dark">The Grey</span>
      <span class="dark">Tide</span>
    </h1>
    <p class="author">
      <span>Pavel</span>
      <span>Arkadievich</span>
      <span>Dorozhkin</span>
    </p>
  </main>
</body>
</html>
```